Designer Instructions – Updated Referral Program Flyer

(Based on the mock-up in “Brief Layout and Instructions.pdf”)

OVERALL STYLE + LAYOUT

Maintain the same general layout, structure, and flow as the mock-up flyer (front and back).

This is an update of an older flyer, not a full redesign — keep the same sections, proportions, and overall visual feel, but with cleaner, more modern design improvements.

The final flyer should look clean, bold, professional, and high-impact, geared toward realtors, property managers, and contractors who refer work.

FRONT SIDE INSTRUCTIONS
1. Header Section

Remove the Tallow Ridge Builders logo from the top banner.
(Shown on page 1 of the PDF)

2. Main Headline

Keep the same three-line structure:
EARN
UNLIMITED
CASH

Center it, maximize impact, and increase the font size of CASH so all three words match in importance.

Make the headline bold, clean, and the main focal point.

3. Cash Incentive Box

Keep the "$500 minimum OR 10% per referral" box, but upgrade the graphics to look sharper and more modern.

Ensure the wording matches exactly what’s in the mock-up.

4. Premier Partner Program Ribbon

Clean up and modernize the "PREMIER PARTNER PROGRAM" bar while keeping the same position and structure.

Ensure the checkmark badge remains crisp and professional.

5. Supporting Icons Section

Keep the four icons/benefit boxes (Guaranteed Payout, Free Evaluations, Affordable Solutions, Industry Leaders) in the same order.

Update the icons to cleaner, more modern styles — but maintain the same meanings.

Improve alignment and spacing for sharper visual consistency.

6. Remove Icons in Contact Area

At the bottom (“CALL TEXT OR BOOK ONLINE 555-014-2796 TallowRidgeBuilders.example”), remove the phone and internet icons, as noted on page 2 of the PDF.

7. Replace All Images

I (Darnell) will provide all updated stock images separately via email.

Replace the flood/water-damage imagery and roof leak with the new images I send.

Keep image placement and proportions the same as the mock-up.

BACK SIDE INSTRUCTIONS
1. Header Image + “REFER / EARN” Section

Maintain the same large split-image layout (“The more you refer, the more you earn”).

Replace all background imagery with the new assets I will send.

Keep the CASH FLOW image section but modernize the type and spacing.

2. “HOW IT WORKS” Section

Preserve the three-column layout:

Refer Flood, Water & Mold Damage

We Take Care of Everything (evaluations/insurance)

Get Paid to Share

Update images, tighten spacing, and use modern iconography.

3. Remove Phone/Internet Icons

Same as the front side — remove small communication icons and keep only the text/number/URL.

4. Bottom Contact Bar

Keep the blue bar, same wording, same layout — just modernize the style if needed for clarity.

5. Replace All Back-Side Images

Again, I will email you the image assets.

Keep the layout EXACT — just update with higher-quality photos and improved design.

TEXT CONTENT (Keep as-is unless spacing adjustments needed)

All text shown in the PDF should remain exactly the same unless spacing or visual balance requires minor adjustments.
Example from page 3:

“REFER FLOOD, MOLD & CONSTRUCTION JOBS”

“We Schedule a Free Estimate. If Approved, You Get Paid.”

“Everybody Benefits From Referrals”

Everything stays, just refreshed and visually improved.

DESIGN GOALS

Flyer should look high-end and trustworthy, not salesy.

Consistent color theme: blues, whites, yellows, same palette as original.

Use bold, modern fonts with strong readability.

Ensure all headlines pop and all benefit boxes are clean, well-aligned, and evenly spaced.

The final result should feel like a premium referral program flyer for a top-tier restoration/remodel company.

FILES I WILL PROVIDE

I will send the designer:

All replacement stock photos

Any updated logos (if needed)

Original high-resolution version of the mock-up (if available)

Any additional icons preferred

0054AA
0677BA
7BADD7
CADEEF
E8F1F8

• Designer Instructions – Updated Referral Program Flyer (Based on the mock-up in “Brief Layout and Instructions.pdf”) OVERALL STYLE + LAYOUT Maintain the same general layout, structure, and flow as the mock-up flyer (front and back). This is an update of an older flyer, not a full redesign — keep the same sections, proportions, and overall visual feel, but with cleaner, more modern design improvements. The final flyer should look clean, bold, professional, and high-impact, geared toward realtors, property managers, and contractors who refer work. FRONT SIDE INSTRUCTIONS 1. Header Section Remove the Tallow Ridge Builders logo from the top banner. (Shown on page 1 of the PDF) 2. Main Headline Keep the same three-line structure: EARN UNLIMITED CASH Center it, maximize impact, and increase the font size of CASH so all three words match in importance. Make the headline bold, clean, and the main focal point. 3. Cash Incentive Box Keep the "$500 minimum OR 10% per referral" box, but upgrade the graphics to look sharper and more modern. Ensure the wording matches exactly what’s in the mock-up. 4. Premier Partner Program Ribbon Clean up and modernize the "PREMIER PARTNER PROGRAM" bar while keeping the same position and structure. Ensure the checkmark badge remains crisp and professional. 5. Supporting Icons Section Keep the four icons/benefit boxes (Guaranteed Payout, Free Evaluations, Affordable Solutions, Industry Leaders) in the same order. Update the icons to cleaner, more modern styles — but maintain the same meanings. Improve alignment and spacing for sharper visual consistency. 6. Remove Icons in Contact Area At the bottom (“CALL TEXT OR BOOK ONLINE 555-014-2796 TallowRidgeBuilders.example”), remove the phone and internet icons, as noted on page 2 of the PDF. 7. Replace All Images I (Darnell) will provide all updated stock images separately via email. Replace the flood/water-damage imagery and roof leak with the new images I send. Keep image placement and proportions the same as the mock-up. BACK SIDE INSTRUCTIONS 1. Header Image + “REFER / EARN” Section Maintain the same large split-image layout (“The more you refer, the more you earn”). Replace all background imagery with the new assets I will send. Keep the CASH FLOW image section but modernize the type and spacing. 2. “HOW IT WORKS” Section Preserve the three-column layout: Refer Flood, Water & Mold Damage We Take Care of Everything (evaluations/insurance) Get Paid to Share Update images, tighten spacing, and use modern iconography. 3. Remove Phone/Internet Icons Same as the front side — remove small communication icons and keep only the text/number/URL. 4. Bottom Contact Bar Keep the blue bar, same wording, same layout — just modernize the style if needed for clarity. 5. Replace All Back-Side Images Again, I will email you the image assets. Keep the layout EXACT — just update with higher-quality photos and improved design. TEXT CONTENT (Keep as-is unless spacing adjustments needed) All text shown in the PDF should remain exactly the same unless spacing or visual balance requires minor adjustments. Example from page 3: “REFER FLOOD, MOLD & CONSTRUCTION JOBS” “We Schedule a Free Estimate. If Approved, You Get Paid.” “Everybody Benefits From Referrals” Everything stays, just refreshed and visually improved. DESIGN GOALS Flyer should look high-end and trustworthy, not salesy. Consistent color theme: blues, whites, yellows, same palette as original. Use bold, modern fonts with strong readability. Ensure all headlines pop and all benefit boxes are clean, well-aligned, and evenly spaced. The final result should feel like a premium referral program flyer for a top-tier restoration/remodel company. FILES I WILL PROVIDE I will send the designer: All replacement stock photos Any updated logos (if needed) Original high-resolution version of the mock-up (if available) Any additional icons preferred

```html
<!DOCTYPE html>
<html lang="en">
<head>
<meta charset="utf-8">
<title>Referral Partner Program Flyer</title>
<link rel="stylesheet" href="https://fonts.googleapis.com/css2?family=Montserrat:wght@400;500;600;700;800;900&display=swap">
<style>
:root{
  --navy:#1a3478;
  --navy-deep:#162c68;
  --blue:#1f6fce;
  --blue-light:#4a9be6;
  --yellow:#ffe500;
  --red:#d42020;
  --white:#ffffff;
  --silver:#c9ccd2;
  --panel:#e3e5ea;
  --ink:#1a3478;
}
*{box-sizing:border-box;margin:0;padding:0}
html,body{width:1200px;height:800px;overflow:hidden;background:var(--white)}
body{font-family:"Montserrat",sans-serif;position:relative}
.flyer{position:absolute;left:33px;top:33px;width:1135px;height:734px;overflow:hidden;background:var(--navy)}
svg text{font-family:"Montserrat",sans-serif}

/* top hero */
.hero{position:absolute;left:0;top:0;width:1135px;height:353px;background:var(--navy)}
.hero__edge{position:absolute;inset:0;background:linear-gradient(180deg,#e9ebef,#9ea3ab);clip-path:polygon(611px 0,1135px 0,1135px 353px,632px 353px,550px 143px)}
.hero__photo{position:absolute;inset:0;background:linear-gradient(160deg,#e8eef3 0%,#bcd0de 45%,#7f9fb6 70%,#4b4e55 100%);clip-path:polygon(625px 0,1135px 0,1135px 353px,646px 353px,564px 143px)}
.hero__license{position:absolute;left:101px;top:12px;width:364px;text-align:center;color:var(--white);font-size:15.5px;font-weight:500;letter-spacing:.1px}
.hero__headline{position:absolute;left:0;top:0}
.hero__tagline{position:absolute;left:0;top:294px;width:640px;height:41px;background:var(--yellow);clip-path:polygon(0 0,624px 0,640px 41px,0 41px)}
.hero__tagline span{position:absolute;left:91px;top:3px;font-size:29.5px;font-weight:900;color:var(--navy);letter-spacing:-.2px}
.hero__badge{position:absolute;left:931px;top:0}

/* lower body */
.body{position:absolute;left:0;top:353px;width:1135px;height:381px;background:radial-gradient(ellipse at 30% 40%,#2f86e0 0%,var(--blue) 45%,#1554ad 100%)}
.incentive{position:absolute;left:62px;top:16px}
.premier{position:absolute;left:621px;top:14px}
.slogan{position:absolute;left:0;top:0}
.benefits{position:absolute;left:63px;top:166px;display:flex;gap:34px}
.benefit{width:227px;height:106px;border-radius:9px;overflow:hidden;box-shadow:0 2px 4px rgba(0,0,0,.35);display:flex;flex-direction:column}
.benefit__title{height:48px;background:var(--navy);color:var(--white);font-weight:800;font-size:17px;line-height:18px;text-align:center;display:flex;align-items:center;justify-content:center;letter-spacing:.2px}
.benefit__body{flex:1;background:linear-gradient(180deg,#c4c7cd,#eceef1 35%,#d9dbe0);display:flex;align-items:center;justify-content:space-between;padding:0 8px 0 24px}
.benefit__text{font-size:12.2px;line-height:14.8px;font-weight:700;color:var(--ink)}
.benefit__icon{flex:none}

/* contact bar */
.contact{position:absolute;left:0;top:323px;width:434px;height:58px;background:var(--navy);clip-path:polygon(0 0,401px 0,434px 58px,0 58px)}
.contact span{position:absolute;left:63px;top:9px;font-size:34px;color:var(--white);font-weight:800;letter-spacing:2.5px;white-space:nowrap}
.contact span em{font-style:normal;font-weight:500}
.contact-line{position:absolute;left:0;top:0}
</style>
</head>
<body>
<main class="flyer">

  <section class="hero">
    <div class="hero__edge"></div>
    <div class="hero__photo" role="img" aria-label="Photo of a bright white kitchen with a blue island, water pouring from the ceiling and flooding the floor"></div>

    <p class="hero__license">Tallow Ridge Builders Inc. CSLB Lic 4820193</p>

    <svg class="hero__headline" width="600" height="300" viewBox="0 0 600 300" aria-label="Earn unlimited cash">
      <text x="102" y="126" fill="var(--yellow)" font-weight="900" font-size="126" textLength="365" lengthAdjust="spacingAndGlyphs">EARN</text>
      <text x="103" y="179" fill="var(--white)" font-weight="900" font-size="56" textLength="349" lengthAdjust="spacingAndGlyphs">UNLIMITED</text>
      <text x="86" y="279" fill="var(--white)" font-weight="900" font-size="131" textLength="378" lengthAdjust="spacingAndGlyphs">CASH</text>
    </svg>

    <div class="hero__tagline"><span>GET PAID TO REFER A FLOOD</span></div>

    <svg class="hero__badge" width="142" height="140" viewBox="0 0 142 140" aria-label="24 hour emergency service">
      <defs><path id="badgeArc" d="M14 76 A57 57 0 0 0 128 76"/></defs>
      <path d="M3 0 H139 V72 A68 68 0 0 1 3 72 Z" fill="var(--white)"/>
      <path d="M6 0 H136 V72 A65 65 0 0 1 6 72 Z" fill="var(--red)"/>
      <circle cx="71" cy="72" r="47" fill="var(--white)"/>
      <circle cx="71" cy="72" r="43" fill="var(--red)"/>
      <text x="71" y="84" text-anchor="middle" fill="var(--white)" font-weight="900" font-size="62" font-style="italic">24</text>
      <text x="71" y="104" text-anchor="middle" fill="var(--white)" font-weight="900" font-size="15">HOUR</text>
      <text fill="var(--red)" font-weight="900" font-size="13" letter-spacing="1"><textPath href="#badgeArc" startOffset="50%" text-anchor="middle">EMERGENCY SERVICE</textPath></text>
    </svg>
  </section>

  <section class="body">

    <svg class="incentive" width="547" height="90" viewBox="0 0 547 90" aria-label="$500 minimum or 10% of total invoice">
      <rect x="0" y="0" width="547" height="88" rx="11" fill="var(--red)"/>
      <circle cx="210" cy="44" r="44" fill="var(--white)"/>
      <text x="117" y="49" text-anchor="middle" fill="var(--white)" font-weight="900" font-size="52" textLength="126" lengthAdjust="spacingAndGlyphs">$500</text>
      <text x="84" y="75" text-anchor="middle" fill="var(--white)" font-weight="900" font-size="23" textLength="114" lengthAdjust="spacingAndGlyphs">MINIMUM</text>
      <text x="210" y="55" text-anchor="middle" fill="var(--navy)" font-weight="900" font-size="31">OR</text>
      <text x="270" y="65" fill="var(--white)" font-weight="900" font-size="64" textLength="127" lengthAdjust="spacingAndGlyphs">10%</text>
      <text x="398" y="42" fill="var(--white)" font-weight="800" font-size="23" textLength="114" lengthAdjust="spacingAndGlyphs">OF TOTAL</text>
      <text x="398" y="63" fill="var(--white)" font-weight="800" font-size="23" textLength="109" lengthAdjust="spacingAndGlyphs">INVOICE</text>
    </svg>

    <svg class="premier" width="456" height="92" viewBox="0 0 456 92" aria-label="Premier partner program">
      <defs>
        <clipPath id="premierShape"><rect x="0" y="0" width="456" height="91" rx="10"/></clipPath>
        <linearGradient id="premierSilver" x1="0" y1="0" x2="0" y2="1"><stop offset="0" stop-color="#d9dbe0"/><stop offset="1" stop-color="#aeb2b9"/></linearGradient>
      </defs>
      <g clip-path="url(#premierShape)">
        <rect x="0" y="0" width="456" height="91" fill="var(--navy)"/>
        <rect x="0" y="28" width="226" height="63" fill="var(--red)"/>
        <rect x="0" y="0" width="456" height="28" fill="url(#premierSilver)"/>
      </g>
      <text x="228" y="22" text-anchor="middle" fill="var(--red)" font-weight="600" font-size="21" letter-spacing="24">PREMIER</text>
      <text x="19" y="72" fill="var(--white)" font-weight="900" font-size="31" letter-spacing="2" textLength="164" lengthAdjust="spacingAndGlyphs">PARTNER</text>
      <text x="268" y="72" fill="var(--white)" font-weight="900" font-size="31" letter-spacing="2" textLength="174" lengthAdjust="spacingAndGlyphs">PROGRAM</text>
      <path d="M228 28 Q248 36 255 30 V60 Q255 80 228 91 Q201 80 201 60 V30 Q208 36 228 28 Z" fill="#c9ccd2"/>
      <path d="M228 33 Q245 40 250 35 V60 Q250 76 228 86 Q206 76 206 60 V35 Q211 40 228 33 Z" fill="var(--white)"/>
      <path d="M215 58 L225 68 L243 48" fill="none" stroke="var(--red)" stroke-width="7" stroke-linecap="round" stroke-linejoin="round"/>
    </svg>

    <svg class="slogan" width="1135" height="330" viewBox="0 0 1135 330" aria-label="Partner with us and everybody wins! Send referrals. Get paid. Grow your business.">
      <text x="68" y="153" fill="var(--white)" font-weight="900" font-size="42" textLength="1001" lengthAdjust="spacingAndGlyphs">PARTNER WITH US &amp; EVERYBODY WINS!</text>
      <text x="63" y="311" fill="var(--white)" font-weight="900" font-size="36" textLength="1014" lengthAdjust="spacingAndGlyphs">SEND <tspan fill="var(--yellow)">REFERRALS.</tspan> GET <tspan fill="var(--yellow)">PAID.</tspan> GROW <tspan fill="var(--yellow)">YOUR BUSINESS.</tspan></text>
    </svg>

    <div class="benefits">
      <article class="benefit">
        <h3 class="benefit__title">EVERYONE<br>CAN REFER</h3>
        <div class="benefit__body" style="padding-left:24px">
          <p class="benefit__text">Plumbers, Contractors,<br>Agents, Roofers<br>&amp; Friends</p>
          <svg class="benefit__icon" width="46" height="46" viewBox="0 0 46 46" aria-hidden="true">
            <circle cx="23" cy="23" r="20" fill="none" stroke="var(--red)" stroke-width="3.5" stroke-dasharray="6 2.5"/>
            <circle cx="23" cy="23" r="14" fill="none" stroke="var(--red)" stroke-width="3"/>
            <path d="M16 23 L21 28 L30 18" fill="none" stroke="var(--red)" stroke-width="4" stroke-linecap="round" stroke-linejoin="round"/>
          </svg>
        </div>
      </article>
      <article class="benefit">
        <h3 class="benefit__title">INSURANCE<br>SPECIALISTS</h3>
        <div class="benefit__body">
          <p class="benefit__text">We Use EstiPro To<br>Secure Clients The<br>Maximum Payout</p>
          <svg class="benefit__icon" width="44" height="50" viewBox="0 0 44 50" aria-hidden="true">
            <rect x="4" y="5" width="28" height="38" rx="3" fill="none" stroke="var(--red)" stroke-width="3"/>
            <rect x="11" y="2" width="14" height="6" rx="2" fill="var(--red)"/>
            <path d="M10 15 H26 M10 21 H26 M10 27 H24 M10 33 H20" stroke="var(--red)" stroke-width="2.5"/>
            <circle cx="33" cy="39" r="9" fill="var(--white)" stroke="var(--red)" stroke-width="2.5"/>
            <text x="33" y="44" text-anchor="middle" fill="var(--red)" font-weight="800" font-size="13">$</text>
          </svg>
        </div>
      </article>
      <article class="benefit">
        <h3 class="benefit__title">AFFORDABLE<br>SOLUTIONS</h3>
        <div class="benefit__body">
          <p class="benefit__text">We Offer Lowest Out<br>of Pocket Costs for<br>Your Customers</p>
          <svg class="benefit__icon" width="54" height="50" viewBox="0 0 54 50" aria-hidden="true">
            <path d="M14 10 Q30 2 50 6 L48 12 Q34 10 24 14 L12 14 Z" fill="none" stroke="var(--red)" stroke-width="2.8" stroke-linejoin="round"/>
            <circle cx="29" cy="25" r="8" fill="none" stroke="var(--red)" stroke-width="2.8"/>
            <text x="29" y="30" text-anchor="middle" fill="var(--red)" font-weight="800" font-size="12">$</text>
            <path d="M4 40 Q20 46 40 42 L46 36 Q38 38 30 38 L20 38" fill="none" stroke="var(--red)" stroke-width="2.8" stroke-linejoin="round"/>
          </svg>
        </div>
      </article>
      <article class="benefit">
        <h3 class="benefit__title">INDUSTRY<br>LEADERS</h3>
        <div class="benefit__body">
          <p class="benefit__text">We are RCIB Certified<br>Licensed General<br>Contractors</p>
          <svg class="benefit__icon" width="46" height="50" viewBox="0 0 46 50" aria-hidden="true">
            <circle cx="23" cy="12" r="8" fill="none" stroke="var(--red)" stroke-width="3"/>
            <path d="M5 46 V34 Q5 24 16 23 H30 Q41 24 41 34 V46 Z" fill="none" stroke="var(--red)" stroke-width="3" stroke-linejoin="round"/>
            <path d="M23 24 L20 30 L23 40 L26 30 Z" fill="var(--red)"/>
            <path d="M13 46 V36 M33 46 V36" stroke="var(--red)" stroke-width="2.5"/>
          </svg>
        </div>
      </article>
    </div>

    <div class="contact"><span>CALL <em>OR</em> TEXT</span></div>
    <svg class="contact-line" width="1135" height="381" viewBox="0 0 1135 381" aria-label="555·014·2796 · TallowRidgeBuilders.example">
      <text x="451" y="369" fill="var(--white)" font-weight="700" font-size="32" letter-spacing="1" textLength="626" lengthAdjust="spacingAndGlyphs">555·014·2796 • TallowRidgeBuilders.example</text>
    </svg>
  </section>

</main>
</body>
</html>
```